Audio Visual & Broadcast Installing Company needs a Web Site Design

We need a website design for our company Corvane Ltd. We are a small company that does Audio Visual and broadcast installations. We are looking to expand our business and need a professional web presence. All work completed by us is done to a very high standard and it’s this attention to detail that sets us apart from our competitors. Our projects include doing fibre optics at major sporting events; installing and commissioning bespoke control systems on super yachts and installing the latest systems in luxury homes.

We provide the following services:
System design
On-site installation
Rack building
Pre-fabricated cable looms
Fibre optic cabling

We would like a website that gives details of our services and provides contact information. Our customers are other businesses and our website needs to reflect this. The flyer attached will be used to promote the company and we would like the website to follow this theme. Please use the colours from our logo, as the colour scheme. We know that our colours are bright and we don’t want them to overwhelm the site. With our website we want to communicate that we are professional and provide a quality service.
NB UPDATE: please use stock images for any graphical elements.

The following 3 sites belong to some of our competitors. The first 2, we DON'T like because they don't project a professional feeling. The last one, 'vellumspire', is better as it provides the required information in a clear, simple form.

http://www.plomquist-example.com/

http://www.heronfieldlinkworks-example.com/

http://www.vellumspire-example.com/

We really like the following site, it feels professional and high end without too many flashy graphics. We want something that is fast to load but still shows the high end quality of our work.

http://osmerdalegroup-example.com/

Pages/Sections

Home
On site installation
Rack building and cable looms
Fibre optics
Portfolio (this will be limited to start with but must be easy to expand and add new projects)
Updates

Target Market(s)

Businesses operating in the following areas:
Audio Vision, Broadcasting, Home Automation, Events

Industry/Entity Type

Broadcasting

Coding

Coded - Design and coding required

Number of Pages Required

4 page

Font styles to use
Other font styles liked:
• similar to attached flyer

Requirements
Must have
• The same theme as the 'flyer1' attachment.

```html
<!DOCTYPE html>
<html lang="en">
<head>
<meta charset="utf-8">
<title>Corvane Ltd – Audio Visual &amp; Broadcast Installation</title>
<link href="https://fonts.googleapis.com/css2?family=Lato:wght@400;700&family=Roboto:wght@400;500&display=swap" rel="stylesheet">
<style>
:root{
  --red:#ee1b34;
  --blue:#3b80f5;
  --blue-dark:#2f6fe6;
  --ink:#222;
  --grey:#555;
  --white:#fff;
}
*{box-sizing:border-box;margin:0;padding:0}
html,body{width:674px;height:1200px;overflow:hidden;background:var(--white)}
body{position:relative;font-family:"Roboto",sans-serif;color:var(--ink)}
.site-header{position:absolute;top:0;left:0;width:674px;height:76px;display:flex;align-items:center;justify-content:center;gap:8px}
.brand-mark{width:14px;height:14px;background:var(--red)}
.brand-name{font-family:"Lato",sans-serif;font-weight:700;font-size:26px;color:var(--ink)}
.main-nav{position:absolute;top:76px;left:0;width:674px;height:29px;background:var(--red);display:flex;padding-left:46px}
.main-nav a{color:var(--white);text-decoration:none;font-size:9.5px;line-height:29px;padding:0 11px;position:relative}
.main-nav a.active::after{content:"";position:absolute;left:0;right:0;bottom:0;height:3px;background:var(--white)}
.backdrop{position:absolute;top:105px;left:0;width:674px;height:905px}
.hero-title{position:absolute;left:56px;top:222px;font-family:"Lato",sans-serif;font-weight:700;font-size:22px;line-height:29px;color:var(--ink)}
.btn{position:absolute;display:flex;align-items:stretch;height:29px;text-decoration:none}
.btn-label{background:var(--blue);color:var(--white);font-family:"Lato",sans-serif;font-size:12.5px;display:flex;align-items:center;padding:0 13px}
.btn-arrow{background:var(--red);width:28px;display:flex;align-items:center;justify-content:center}
.hero-btn{left:55px;top:294px}
.hero-btn .btn-label{width:99px}
.slide-arrow{position:absolute;top:255px;width:28px;height:28px;border:1px solid rgba(60,60,60,.6);border-radius:50%;background:rgba(255,255,255,.35);display:flex;align-items:center;justify-content:center;font-size:13px;color:#333}
.slide-prev{left:8px}
.slide-next{left:638px;border-color:#fff;color:#fff;background:rgba(0,0,0,.25)}
.service-label{position:absolute;color:var(--white);font-family:"Lato",sans-serif;font-weight:700;font-size:11.5px;text-align:center;line-height:16px}
.intro{position:absolute;left:0;top:818px;width:674px;text-align:center;color:var(--white)}
.intro h1{font-family:"Lato",sans-serif;font-weight:400;font-size:22px;line-height:29px;margin-bottom:10px}
.intro p{font-size:8.5px;line-height:14px;width:420px;margin:0 auto 7px}
.footer-brand{position:absolute;left:44px;top:1080px;display:flex;align-items:center;gap:8px}
.footer-brand .brand-name{font-size:30px}
.footer-col h2{font-family:"Lato",sans-serif;font-weight:400;font-size:14px;color:var(--grey);margin-bottom:13px}
.contact-info{position:absolute;left:247px;top:1043px;width:170px}
.contact-info li{list-style:none;display:flex;gap:9px;font-size:8.5px;line-height:13px;color:var(--grey);margin-bottom:10px}
.contact-info svg{flex:none;margin-top:1px}
.newsletter{position:absolute;left:450px;top:1043px}
.newsletter input{display:block;width:141px;height:23px;border:1px solid #ccc;font-family:"Roboto",sans-serif;font-size:8.5px;padding:0 5px;color:var(--grey);margin-bottom:9px}
.newsletter .btn{position:static}
.newsletter .btn-label{width:79px;font-size:11.5px}
.footer-bar{position:absolute;left:0;top:1170px;width:674px;height:30px;background:var(--blue);color:var(--white);font-size:8.5px;text-align:center;line-height:30px}
</style>
</head>
<body>
<header class="site-header">
  <span class="brand-mark"></span><span class="brand-name">Corvane</span>
</header>
<nav class="main-nav">
  <a class="active" href="#">Home</a>
  <a href="#">On Site Installation</a>
  <a href="#">Rack Building and Cable Looms</a>
  <a href="#">Fiber Optics</a>
  <a href="#">Portfolio</a>
  <a href="#">Contact</a>
</nav>

<svg class="backdrop" width="674" height="905" viewBox="0 105 674 905">
  <defs>
    <linearGradient id="heroPhoto" x1="0" y1="0" x2="1" y2="1">
      <stop offset="0" stop-color="#d9dde3"/><stop offset=".5" stop-color="#a9afb8"/><stop offset="1" stop-color="#3b3f4a"/>
    </linearGradient>
    <linearGradient id="servicesBand" x1="0" y1="0" x2="1" y2="0">
      <stop offset="0" stop-color="#e8213d"/><stop offset=".5" stop-color="#8b3fa6"/><stop offset="1" stop-color="#3a7ff2"/>
    </linearGradient>
  </defs>
  <rect role="img" aria-label="Photo of a broadcast mixing console" x="0" y="105" width="674" height="400" fill="url(#heroPhoto)"/>
  <path role="img" aria-label="Photo of a stadium crowd tinted red to blue" d="M0,430 Q250,480 674,428 L674,1010 L0,1010 Z" fill="url(#servicesBand)"/>
  <path d="M0,815 Q337,740 674,815 L674,1010 L0,1010 Z" fill="var(--blue)"/>
  <g stroke="#fff" stroke-width="3">
    <line x1="337" y1="505" x2="182" y2="534"/><line x1="337" y1="505" x2="246" y2="612"/>
    <line x1="337" y1="505" x2="337" y2="663"/><line x1="337" y1="505" x2="424" y2="606"/>
    <line x1="337" y1="505" x2="493" y2="536"/>
  </g>
  <circle cx="337" cy="505" r="72" fill="#fff"/>
  <circle cx="337" cy="505" r="66" fill="none" stroke="var(--red)" stroke-width="2"/>
  <text x="337" y="511" text-anchor="middle" font-family="Lato, sans-serif" font-weight="700" font-size="17" fill="#222">Corvane</text>
  <g fill="#fff" stroke="var(--blue)" stroke-width="2">
    <circle cx="182" cy="534" r="40"/><circle cx="246" cy="612" r="40"/>
    <circle cx="337" cy="663" r="40"/><circle cx="424" cy="606" r="40"/>
    <circle cx="493" cy="536" r="40"/>
  </g>
  <g fill="none" stroke="var(--blue)" stroke-width="2.5" stroke-linecap="round">
    <path d="M182,521 v16 M175,531 l7,7 l7,-7 M166,538 v6 h32 v-6"/>
    <path d="M246,620 v10 M242,620 h8 M246,620 l-8,-14 M246,620 l8,-14 M246,620 v-16"/>
    <path d="M337,676 l-7,-18 h14 z M337,658 v-4 M329,650 a10,10 0 0 1 16,0 M324,645 a16,16 0 0 1 26,0"/>
    <rect x="410" y="600" width="28" height="12" rx="6"/><rect x="416" y="603" width="18" height="6" rx="3"/>
    <rect x="479" y="522" width="28" height="8"/><rect x="479" y="532" width="28" height="8"/><rect x="479" y="542" width="28" height="8"/>
  </g>
</svg>

<h2 class="hero-title">Brodcasting Elmcourt was equally<br>thrilling as playing Elmcourt.</h2>
<a class="btn hero-btn" href="#"><span class="btn-label">CONTACT US</span><span class="btn-arrow"><svg width="10" height="14"><path d="M2,1 L8,7 L2,13" fill="none" stroke="#fff" stroke-width="2.5"/></svg></span></a>
<span class="slide-arrow slide-prev">«</span>
<span class="slide-arrow slide-next">»</span>

<span class="service-label" style="left:31px;top:538px">On-site installation</span>
<span class="service-label" style="left:70px;top:620px">Fiber Optic Installation</span>
<span class="service-label" style="left:272px;top:714px;width:130px">Brodcast/ AV System<br>Design</span>
<span class="service-label" style="left:479px;top:620px">Pre-fabricated Cable Looms</span>
<span class="service-label" style="left:546px;top:538px">Rack Building</span>

<section class="intro">
  <h1>Making the connections that digital<br>innovation demands</h1>
  <p>Our Projects range from fiber optic cabling at major sport events to installing and commoisioning bespoke bekpose control system on some of worlds largest super yatches. The Company based in london has executed projects succesfully across europ.</p>
  <p>Corvane provide cabling seervoces for Brodcast Television and Audio Visual Systems. With over 15 Years experiance working in these industries we can help with every espects of design, project management, installtion and maintenance</p>
</section>

<div class="footer-brand"><span class="brand-mark"></span><span class="brand-name">Corvane</span></div>
<div class="footer-col contact-info">
  <h2>Contact Info</h2>
  <ul>
    <li><svg width="10" height="12"><path d="M5,11 C1,6 1,4 1,4 a4,4 0 0 1 8,0 C9,4 9,6 5,11z" fill="#555"/><circle cx="5" cy="4" r="1.5" fill="#fff"/></svg>123 Street, Land mark, Country 1234567</li>
    <li><svg width="10" height="11"><path d="M2,1 l2,0 l1,3 l-1.5,1 a6,6 0 0 0 3,3 l1,-1.5 l3,1 l0,2 a8,8 0 0 1 -8.5,-8.5z" fill="#555"/></svg>01234 123 4567</li>
    <li><svg width="10" height="9"><rect x=".5" y="1" width="9" height="7" fill="none" stroke="#555"/><path d="M.5,1 l4.5,4 l4.5,-4" fill="none" stroke="#555"/></svg>info@corvane-example.com</li>
  </ul>
</div>
<div class="footer-col newsletter">
  <h2>Newsletter</h2>
  <input type="email" placeholder="Enter Email Id" aria-label="Email address">
  <a class="btn" href="#"><span class="btn-label">SUBSCRIBE</span><span class="btn-arrow"><svg width="10" height="14"><path d="M2,1 L8,7 L2,13" fill="none" stroke="#fff" stroke-width="2.5"/></svg></span></a>
</div>
<footer class="footer-bar">©Corvane Ltd. 2017 - All Rights Reserved.</footer>
</body>
</html>
```